Pill bottle label - clearly defined niche

UPDATE 02/01/19 - VERY IMPORTANT - SEE LATEST ATTACHMENT FOR A SIGNIFICANT UPDATE TO THE BRIEF - Word Doc: "Brief Update V1.3"

I need a striking design for a vitamin/supplement bottle. The purpose of the supplement is to help the body fight the effects of airborne pollution. It will initially be targeted to the China market. The product will be named Haze Warden. I want to get away from the generic look of vitamin bottles and use an illustrated character, probably an animal, as I think it is more memorable and gender neutral. The strap line will be "Fight" or more likely, "Fight Back".The product will contain a combination of B, C, D & E vitamins AND Traditional Chinese Medicine (TCM) ingredients such as ginseng, astragalus and ginkgo leaf. Therefore, we need to say that this product is bringing together the best of East and West to protect against the effects of smog.Recap of elements;Name: Haze WardenStrap Line: Fight Back(the name and strap will also need to appear in Chinese (maybe in a narrow band around the top of the label?)Character: Illustration of cute Chinese fighting character (human or animal) OR maybe a giraffe with his head above the smog clouds. Wide open to ideas.Company Name: just put ORVIN Ltd. for now!Ingredients panel, Barcode, QR codeOther sources for visual inspiration are air-pollution apps - most popular one is Sky Ledger sky-ledger.example.I have a Snapboard page where I've saved some nice bottle/label designs and some visuals that might inspire for the character - https://www.snapboard.example/tolandreeve/packaging/vitamins/
Updates

Bad time of year with Christmas and New Year affecting our timeline. To get more designs and have the time to review and respond we need to allow more time. Even the 4th is a bit tight with new years eve/day in the middle of it. Ideally, I would make the deadline the 7th, which would allow that weekend to be included.

Please ensure you view the latest brief update (attached as a Word doc) in Projects.

Target Market(s)

Chinese consumers

Industry/Entity Type

Supplement

Requirements
Must have
• UPDATE 02/01/19 - VERY IMPORTANT - SEE LATEST ATTACHMENT FOR A SIGNIFICANT UPDATE TO THE BRIEF
• Brief V1.2
• In terms of strategic marketing message conveyed by the strap line, I have two different routes we could go down.
• The first is the more "aggressive" route (fight back), currently symbolised by the fighting character.
• The second is the "clever" route, currently symbolised by the giraffe with its head above the smog clouds. The "fight back" strap line will not work with the giraffe. If we were to go down the "smart" route, we will use a strap line like "Be Smart"
• There may be a third route which combines the two approaches. If we were to have a strap line of "Fight Smart" it might be possible to use the gentle intelligent giraffe character but add a martial arts headband.
• Looking at the imagery - I like this one. That doesn't mean you have to use it! I still want to see creativity and originality. But, a stylised version with a giraffe in a headband and another with sunglasses on, might work well. I could see the bottom half of the label being cloudy and murky and it being bright and sunny up top.
Nice to have

```html
<!DOCTYPE html>
<html lang="en">
<head>
<meta charset="utf-8">
<title>Haze Warden – Label</title>
<link href="https://fonts.googleapis.com/css2?family=Fira+Sans:ital,wght@0,400;0,500;0,600;0,800;1,200&family=Archivo:wght@400;600;800&family=Noto+Sans+SC:wght@400;500&display=swap" rel="stylesheet">
<style>
:root{
  --orange:#e8821e;
  --orange-deep:#d9700f;
  --ink:#2a2a2a;
  --charcoal:#3a3a3c;
  --paper:#ffffff;
  --stripe:#eeeeee;
  --bg:#f4f4f4;
  --rule:#111;
}
*{box-sizing:border-box;margin:0;padding:0}
html,body{width:1200px;height:948px;overflow:hidden;background:var(--bg)}
body{position:relative;font-family:"Fira Sans",sans-serif;color:var(--ink)}
.label{position:absolute;top:150px;width:380px;height:660px;
  background:linear-gradient(90deg,var(--paper),var(--stripe) 50%,var(--paper));
  border-top:22px solid var(--orange);overflow:hidden;box-shadow:0 2px 10px rgba(0,0,0,.08)}
.label--back{left:20px}
.label--front{left:410px}
.label--facts{left:800px}
.band-bottom{position:absolute;left:0;right:0;bottom:0;height:78px;background:var(--orange);
  color:var(--paper);font-weight:600;font-size:20px;display:flex;align-items:center;padding:0 20px}

/* back panel */
.info{position:absolute;left:22px;right:22px;top:70px;font-size:10px;line-height:1.35}
.info h4{font-size:9.5px;font-weight:500;margin-top:18px}
.info h4:first-child{margin-top:0}
.info p{color:#333}
.claim{margin-top:24px;border:2px solid var(--ink);padding:12px 20px;text-align:center;font-size:10px;text-transform:uppercase}
.exp{justify-content:flex-end}

/* front panel */
.tab{position:absolute;left:0;top:0;width:380px;height:110px}
.cn-name{position:absolute;top:4px;width:100%;text-align:center;font-family:"Noto Sans SC",sans-serif;color:var(--paper);font-size:38px;font-weight:400;letter-spacing:1px}
.cn-strap{position:absolute;top:52px;width:100%;text-align:center;font-family:"Noto Sans SC",sans-serif;color:var(--paper);font-size:34px;font-weight:400}
.brand{position:absolute;left:24px;top:145px;font-size:46px;font-weight:800;color:var(--orange);letter-spacing:-.5px;line-height:1;white-space:nowrap}
.strap{position:absolute;left:24px;top:200px;font-size:50px;font-weight:200;font-style:italic;color:var(--ink);line-height:1;white-space:nowrap}
.herbs{position:absolute;left:24px;top:278px;list-style:none;z-index:2}
.herbs li{display:flex;align-items:center;gap:6px;font-size:29px;font-weight:500;color:var(--orange);height:46px;white-space:nowrap}
.herb-icon{width:28px;height:28px;border-radius:50%;border:1.5px solid #9a9a9a;background:#dfe8c8;flex:none}
.mascot{position:absolute;right:6px;top:318px;width:130px;height:230px;border-radius:60px;
  background:linear-gradient(180deg,#2b2b2b 0 45%,var(--orange) 45% 100%);z-index:1}
.formula{position:absolute;left:0;top:440px;width:300px;height:66px;background:var(--charcoal);color:var(--paper);
  font-size:15.5px;font-weight:500;line-height:1.3;padding:11px 0 0 22px;border-top-right-radius:14px;white-space:nowrap;z-index:2}
.count{position:absolute;left:0;right:0;bottom:0;height:82px;background:var(--orange);color:var(--paper);display:flex;align-items:center;padding-left:24px;gap:6px}
.count b{font-size:44px;font-weight:400}
.count span{font-size:18px;font-weight:500;line-height:1.05;text-transform:uppercase}

/* facts panel */
.facts{position:absolute;left:16px;right:16px;top:28px;font-family:"Archivo",sans-serif;font-size:8.5px;line-height:1.35}
.facts h3{font-size:19px;font-weight:800;letter-spacing:-.3px;border-bottom:1px solid var(--rule);white-space:nowrap}
.row{display:flex;justify-content:space-between;border-bottom:1px solid #999;padding:1px 0}
.row.strong{font-weight:600}
.row.indent{padding-left:10px;color:#444}
.row.indent2{padding-left:18px;color:#444}
.thick{border-bottom:7px solid var(--rule)}
.mid{border-bottom:4px solid var(--rule)}
.cal{display:flex;justify-content:space-between;align-items:flex-end;font-size:17px;font-weight:800}
.cal small{font-size:6px;font-weight:400;display:block}
.dv{text-align:right;font-size:6px;border-bottom:1px solid #999}
.foot{font-size:6px;padding-top:3px;color:#333}
.blurb{position:absolute;left:16px;right:16px;top:470px;font-size:12px;line-height:1.25}
.contact{font-size:13.5px;white-space:nowrap;padding:0 14px}
</style>
</head>
<body>

<section class="label label--back">
  <div class="info">
    <h4>Other Ingredients:</h4>
    <p>Lorem ipsum dolor sit amet, consectetuer adipiscing elit, sed diam nonummy nibh euismod tincidunt ut laoreet</p>
    <h4>Benefits:</h4>
    <p>Lorem ipsum dolor sit amet, consectetuer adipiscing elit, sed diam nonummy nibh euismod tincidunt ut laoreet dolore magna aliquam erat volutpat. Ut wisi enim ad minim veniam</p>
    <h4>Warnings:</h4>
    <p>Lorem ipsum dolor sit amet, consectetuer adipiscing elit, sed diam nonummy nibh euismod tincidunt ut laoreet dolore magna aliquam erat volutpat. Ut wisi enim ad minim veniam</p>
    <h4>Storage Condition:</h4>
    <p>Keep container tightly sealed in a cool and dry place. Avoide heat and light.</p>
    <h4>PRECAUTIONS:</h4>
    <p>DO NOT USE THIS PRODUCT IF SAFETY SEAL IS MISSING OR BROKEN<br>KEEP OUT OF REACH OF CHILDREN.</p>
    <div class="claim">This product is bringing together the best of<br>East and West to protect against the effects of smog.</div>
  </div>
  <div class="band-bottom exp">Exp Date:</div>
</section>

<section class="label label--front">
  <svg class="tab" viewBox="0 0 380 110" aria-hidden="true">
    <path d="M70 0 H310 Q300 95 240 105 H140 Q80 95 70 0 Z" fill="var(--orange)"/>
  </svg>
  <div class="cn-name">霾守衛</div>
  <div class="cn-strap">回擊</div>
  <h1 class="brand">HAZE WARDEN</h1>
  <p class="strap">FIGHT BACK</p>
  <ul class="herbs">
    <li><span class="herb-icon" role="img" aria-label="Ginseng root icon"></span>Ginseng</li>
    <li><span class="herb-icon" role="img" aria-label="Astragalus plant icon"></span>Astragalus</li>
    <li><span class="herb-icon" role="img" aria-label="Ginkgo leaf icon"></span>Ginkgo Leaf</li>
  </ul>
  <div class="mascot" role="img" aria-label="Cartoon ninja character in a fighting stance with a sword, over an orange circle"></div>
  <div class="formula">Vitamins B, C, D &amp; E &amp;<br>Traditional Chinese Medicine (TCM)</div>
  <div class="count"><b>60</b><span>Vegetarian<br>Capsule</span></div>
</section>

<section class="label label--facts">
  <div class="facts">
    <h3>Nutrition Facts/Datos de Nutrición</h3>
    <div>8 servings per container/8 raciónes por envase</div>
    <div class="row strong thick" style="font-size:10px"><span>Serving size/Tamaño por ración</span><span>2/3 cup/2/3 taza (55g)</span></div>
    <div class="cal mid"><span><small>Amount per serving/Cantidad por ración</small>Calories/Calorías</span><span>230</span></div>
    <div class="dv">% Daily Value*/Valor Diario*</div>
    <div class="row strong"><span>Total Fat/Grasa Total 8g</span><span>10%</span></div>
    <div class="row indent"><span>Saturated Fat/Grasa Saturada 1g</span><span>5%</span></div>
    <div class="row indent"><span>Trans Fat/Grasa Trans 0g</span><span></span></div>
    <div class="row strong"><span>Cholesterol/Colesterol 0mg</span><span>0%</span></div>
    <div class="row strong"><span>Sodium/Sodio 160mg</span><span>7%</span></div>
    <div class="row strong"><span>Total Carbohydrate/Carbohidrato Total 37g</span><span>13%</span></div>
    <div class="row indent"><span>Dietary Fiber/Fibra Dietética 4g</span><span>14%</span></div>
    <div class="row indent"><span>Total Sugars/Azúcares Total 12g</span><span></span></div>
    <div class="row indent2"><span>Includes 10g Added Sugars/Incluye 10g azúcares añadidos</span><span>20%</span></div>
    <div class="row strong thick"><span>Protein/Proteínas 3g</span><span></span></div>
    <div class="row"><span>Vitamin D/Vitamina D 2mcg</span><span>10%</span></div>
    <div class="row"><span>Calcium/Calcio 260mg</span><span>20%</span></div>
    <div class="row"><span>Iron/Hierro 8mg</span><span>45%</span></div>
    <div class="row mid"><span>Potassium/Potasio 235mg</span><span>6%</span></div>
    <p class="foot">* The % Daily Value tells you how much a nutrient in a serving adds to a daily diet. 2,000 calories a day is used for general advice.</p>
    <p class="foot">* El % Valor Diario indica cuánto un nutriente aporta a una dieta diaria. Se usan 2,000 calorías al día.</p>
  </div>
  <p class="blurb">Lorem ipsum dolor sit amet, cons ectetuer adipiscing elit, sed diam nonummy nibh euismod tincidunt ut laoreet dolore magna aliquam erat volutpat. Ut wisi enim ad minim veniam, quis nostrud exerci tation ullamcorper suscipit lobortis nisl ut aliquip ex ea commodo consequat.</p>
  <div class="band-bottom contact">ORVIN Ltd | www.orvinltd.example | 000 0000 00</div>
</section>

</body>
</html>
```